I need a business card representing my company, VELDAR, it's an artist management and design company. Complete name is "VELDAR Artist Mgmt. + Design Co." I need it to be world class and very appealing, sophisticated and artistically unique.
Updates

Posted an updated Brief please see. I need a business card representing my company, VELDAR, it's an artist management and design company. Complete name is "VELDAR Artist Mgmt. + Design Co." I need it to be world class and very appealing, sophisticated and artistically unique.

Designs look the same

Designs look the same

Target Market(s)

Advertisers, Entertainment Companies, Commercial companies

Industry/Entity Type

Advertising

Contact Information for Business Card

I need a business card representing my company, VELDAR, it's an artist management and design company. Complete name is "VELDAR Artist Mgmt. + Design Co." I need it to be world class and very appealing, sophisticated and artistically unique. One side can be VELDAR Artist Mgmt. + Design Co. and the other my name, Theodore Quillan, my contact telephone: 415.638.2097, email veldarartist@mailnest.example, my address: 2416 Harrowgate Ave. #317 Miami, FL 33152

Font styles to use
Other font styles liked:
• Calibri

Colors
ffffff
0455a3
f37122

Requirements
Must have
• "VELDAR" stand out bigger than the rest of the text.
Nice to have
• Name "VELDAR" can be centered on one side or in the corner or along side edges, just need something cool and different.
Should not have
• I am open just try to keep it clean looking

```html
<!DOCTYPE html>
<html lang="en">
<head>
<meta charset="utf-8">
<title>VELDAR Business Card</title>
<link href="https://fonts.googleapis.com/css2?family=Questrial&family=Mulish:wght@700&display=swap" rel="stylesheet">
<style>
  :root {
    --page: #ffffff;
    --card-white: #ffffff;
    --navy: #231087;
    --navy-deep: #0d0552;
    --navy-glow: #2c0fa8;
    --ink: #2a1a8c;
    --accent-pink: #e8177f;
    --text-light: #ffffff;
    --border: #b9b9c4;
  }
  * { box-sizing: border-box; margin: 0; padding: 0; }
  html, body {
    width: 1200px; height: 403px; overflow: hidden;
    background: var(--page);
    font-family: "Questrial", "Century Gothic", sans-serif;
  }
  .canvas { position: relative; width: 1200px; height: 403px; }

  .card {
    position: absolute; top: 38px;
    width: 561px; height: 322px;
    border: 1px solid var(--border);
    overflow: hidden;
  }
  .card--front { left: 32px; background: var(--card-white); }
  .card--back { left: 609px; }

  /* front */
  .brand {
    position: absolute; left: 21px; top: 18px;
    display: flex; align-items: center; gap: 8px;
  }
  .brand__square { width: 22px; height: 22px; background: var(--accent-pink); border-radius: 3px; }
  .brand__name { font-size: 22px; color: var(--navy); letter-spacing: 1px; }

  .person {
    position: absolute; left: 146px; top: 124px; width: 268px;
    text-align: center; color: var(--ink);
  }
  .person__name {
    font-size: 26px; line-height: 1.3;
    border-bottom: 2px solid var(--ink);
    padding-bottom: 2px;
  }
  .person__title { font-size: 17px; margin-top: 3px; letter-spacing: .5px; }

  .contact-band {
    position: absolute; left: 0; bottom: 0; width: 100%; height: 72px;
    background: radial-gradient(ellipse at 62% 50%, var(--navy-glow) 0%, var(--navy) 45%, var(--navy-deep) 100%);
    color: var(--text-light);
  }
  .address {
    position: absolute; left: 28px; top: 19px; width: 280px;
    text-align: center; font-size: 14px; line-height: 19px;
  }
  .phones { position: absolute; left: 354px; top: 9px; font-size: 14px; line-height: 19.5px; }
  .phones__row { display: flex; }
  .phones__label { width: 54px; }
  .phones__number { font-family: "Mulish", "Century Gothic", sans-serif; font-weight: 700; }

  /* back */
  .back-backdrop {
    position: absolute; inset: 0;
    background:
      radial-gradient(ellipse at 50% 75%, rgba(120, 100, 230, .35) 0%, rgba(60, 30, 180, 0) 60%),
      linear-gradient(90deg, var(--navy-deep) 0%, var(--navy-glow) 50%, var(--navy-deep) 100%);
  }
  .back-brand {
    position: absolute; left: 0; right: 0; top: 118px;
    display: flex; justify-content: center; align-items: center; gap: 12px;
  }
  .back-brand__square { width: 34px; height: 34px; background: var(--accent-pink); border-radius: 4px; }
  .back-brand__name { font-size: 40px; color: var(--text-light); letter-spacing: 2px; }
  .email {
    position: absolute; left: 0; right: 0; top: 262px;
    text-align: center; font-size: 27px; color: var(--text-light);
  }
</style>
</head>
<body>
<main class="canvas">
  <section class="card card--front" aria-label="Card front">
    <div class="brand">
      <span class="brand__square"></span>
      <span class="brand__name">VELDAR</span>
    </div>
    <div class="person">
      <h1 class="person__name">Theodore Quillan</h1>
      <p class="person__title">MANANGER</p>
    </div>
    <div class="contact-band">
      <p class="address">Harrowgate Avenue, Studio 317<br>Miami, Florida 33152</p>
      <div class="phones">
        <p class="phones__row"><span class="phones__label">Office:</span><span class="phones__number">415-638-2210</span></p>
        <p class="phones__row"><span class="phones__label">Direc:</span><span class="phones__number">415-638-2097</span></p>
        <p class="phones__row"><span class="phones__label">Fax:</span><span class="phones__number">415-638-2218</span></p>
      </div>
    </div>
  </section>

  <section class="card card--back" aria-label="Card back">
    <div class="back-backdrop" role="img" aria-label="Deep blue perspective grid floor receding to a vanishing point"></div>
    <div class="back-brand">
      <span class="back-brand__square"></span>
      <span class="back-brand__name">VELDAR</span>
    </div>
    <p class="email">tquillan@veldarart.example</p>
  </section>
</main>
</body>
</html>
```